Private practice for psychiatry and psychotherapy needs a business card and logo

I need a logo and business card design for my private practice for psychiatry and psychotherapy. The optional names for my practice are: Voskuilen Praktijk voor Psychiatrie en Psychotherapie, or short: Praktijk Voskuilen.
I am a (child and adolescent) psychiatrist and psychotherapist. I diagnose and treat infants, children, adolescents and adults with psychiatric symptoms/disorders. I also give supervision to colleagues about their own treatments. My work is characterised by personal involvement, transparence, creativity and professionality.
I would like to have an appealing, light and bright, yet basic design that invites people (both children and adults) to contact me, gives trust and hope, without loosing professional appearance.
I uploaded my contact information which should not necessarily be all included (in this form) on the card as long as people know how to contact me. Please feel free to be creative!
Please note that my website is only temporarely and need a new design and update too!

Target Market(s)

Clients and patients (children, adolescents, adults) with psychiatric symptoms who need diagnosis and treatment. I work with private clients and patients through medical insurances.

Industry/Entity Type

Mental Health

Contact Information for Business Card

Dr. Femke Voskuilen-ter Horst
Psychiater/Kinder- en Jeugdpsychiater
Gerrit Wassinkstraat 4
3063 TW Rotterdam
t: 06-58190274
e: info@praktijkvoskuilen-voorbeeld.nl
i: www.praktijkvoskuilen-voorbeeld.nl

Logo Text

Praktijk Voskuilen voor Psychiatrie en Psychotherapie; or short: Praktijk Voskuilen

Font styles to use
Sans Serif
Other font styles liked:
• up to designer

Requirements
Must have
• Appealing, light, bright, creative, trustful, professional and unique.

```html
<!DOCTYPE html>
<html lang="nl">
<head>
<meta charset="utf-8">
<title>Praktijk Voskuilen – visitekaartje</title>
<link href="https://fonts.googleapis.com/css2?family=Italianno&family=Questrial&display=swap" rel="stylesheet">
<style>
  :root {
    --ink: #111111;
    --paper: #ffffff;
    --rule: #111111;
  }
  html, body {
    margin: 0;
    padding: 0;
    overflow: hidden;
    background: var(--paper);
  }
  .canvas {
    position: relative;
    width: 1050px;
    height: 1200px;
    background: var(--paper);
    color: var(--ink);
    overflow: hidden;
  }
  .card-front, .card-back {
    position: absolute;
    left: 0;
    width: 1050px;
  }
  .card-front { top: 0; height: 610px; }
  .card-back { top: 613px; height: 587px; }
  .card-divider {
    position: absolute;
    left: 0;
    top: 609px;
    width: 1050px;
    height: 3px;
    background: var(--rule);
  }
  .practice-name {
    position: absolute;
    display: flex;
    align-items: center;
    justify-content: center;
    font-family: "Questrial", sans-serif;
    color: var(--ink);
    text-align: center;
    line-height: 1.15;
  }
  .practice-name--front {
    left: 370px;
    top: 95px;
    width: 310px;
    height: 250px;
    font-size: 40px;
  }
  .practice-name--back {
    left: 715px;
    top: 252px;
    width: 310px;
    height: 245px;
    font-size: 34px;
  }
  .service-title {
    position: absolute;
    left: 0;
    top: 392px;
    width: 1050px;
    text-align: center;
    font-family: "Italianno", cursive;
    font-size: 96px;
    letter-spacing: 2px;
    line-height: 1;
  }
  .person-name {
    position: absolute;
    left: 0;
    top: 80px;
    width: 1050px;
    text-align: center;
    font-family: "Italianno", cursive;
    font-size: 92px;
    line-height: 1;
  }
  .contact {
    position: absolute;
    left: 55px;
    top: 260px;
    margin: 0;
    font-family: "Questrial", sans-serif;
    font-size: 31px;
    line-height: 37.5px;
    font-style: normal;
  }
  .contact span { display: block; }
</style>
</head>
<body>
<div class="canvas">
  <section class="card-front">
    <div class="practice-name practice-name--front">Praktijk<br>Voskuilen</div>
    <div class="service-title">PSYCHOTHERAPIE</div>
  </section>

  <div class="card-divider"></div>

  <section class="card-back">
    <div class="person-name">Dr. Femke Voskuilen-ter Horst</div>
    <address class="contact">
      <span>Psychiater/Kinder- en Jeugdpsychiater</span>
      <span>Gerrit Wassinkstraat 4</span>
      <span>3063 TW Rotterdam</span>
      <span>t: 06-58190274</span>
      <span>e: info@praktijkvoskuilen-voorbeeld.nl</span>
      <span>i: www.praktijkvoskuilen-voorbeeld.nl</span>
    </address>
    <div class="practice-name practice-name--back">Praktijk<br>Voskuilen</div>
  </section>
</div>
</body>
</html>
```